Brixom Vale needs a powerpoint design

We need a powerpoint design for an Information Technology based in Fairfax call "Brixom Vale". We are Information Technology solutions provider for the Federal Government. We develop Talvex, Mobile and Cloud based solutions. We support the Healthcare and Financial sectors of the Government. We would like to see designs that use the colors of our logo. We've attached a copy of our logo. The final design should communicate Information Technology and System Integration with Agile Development.

Target Market(s)

Our target market is the Federal Government and System Integators in the Washington DC area.

Industry/Entity Type

Government

Requirements
Must have
• The powerpoint design must have a professional look.

```html
<!DOCTYPE html>
<html lang="en">
<head>
<meta charset="utf-8">
<title>Brixom Vale – Slide Template</title>
<link href="https://fonts.googleapis.com/css2?family=Open+Sans:wght@400;600;700;800&display=swap" rel="stylesheet">
<style>
  :root{
    --page:#e6eaef;
    --blue:#1565b8;
    --blue-deep:#0b3f86;
    --blue-bright:#1e88d8;
    --ink:#222831;
    --muted:#5a6470;
    --grey-light:#f4f5f6;
    --grey:#c9ccd0;
    --accent:#b7d93a;
    --pie-blue:#1a6dc2;
    --pie-blue-dark:#0f4c91;
    --pie-grey:#8a8d92;
    --pie-grey-dark:#63666b;
    --pie-silver:#b2b5b9;
    --pie-silver-dark:#8d9094;
    --pie-sky:#23a5e6;
    --pie-sky-dark:#1682b8;
  }
  *{box-sizing:border-box;margin:0;padding:0}
  html,body{width:712px;height:1200px;overflow:hidden}
  body{background:var(--page);font-family:"Open Sans",Arial,sans-serif;color:var(--ink)}
  .deck{display:flex;flex-direction:column;align-items:center;gap:18.75px;padding-top:18.75px}
  .slide{position:relative;width:500px;height:375px;overflow:hidden;box-shadow:0 2px 8px rgba(0,0,0,.25)}

  /* Slide 1 — cover mark */
  .slide-cover{background:radial-gradient(ellipse at 50% 45%,#ffffff 0%,#f1f2f3 55%,#d9dbde 100%)}
  .cover-brand{position:absolute;top:150px;left:0;right:0;display:flex;justify-content:center;align-items:center;gap:12px}
  .brand-square{width:26px;height:26px;background:var(--blue)}
  .cover-name{font-size:34px;font-weight:700;color:var(--blue)}
  .cover-url{position:absolute;bottom:26px;left:0;right:0;text-align:center;font-size:8px;color:var(--ink)}

  /* Slide 2 — title */
  .slide-title{background:linear-gradient(#ffffff,#e3e5e8 22%)}
  .title-head{position:absolute;top:28px;left:0;right:0;display:flex;justify-content:center;align-items:center;gap:7px}
  .title-head .brand-square{width:14px;height:14px}
  .title-head-name{font-size:15px;font-weight:700;color:var(--blue)}
  .title-band{position:absolute;top:78px;left:0;right:0;height:180px;
    background:linear-gradient(180deg,var(--blue-deep) 0%,var(--blue-bright) 45%,var(--blue) 70%,var(--blue-deep) 100%);
    display:flex;flex-direction:column;justify-content:center;align-items:center;gap:8px}
  .title-main{font-size:27px;font-weight:600;color:#fff;letter-spacing:.3px}
  .title-sub{font-size:9px;font-weight:800;color:var(--accent);letter-spacing:.6px}
  .title-foot{position:absolute;top:285px;left:0;right:0;text-align:center;font-size:7.5px;line-height:20px}
  .title-url{color:var(--ink)}
  .title-copy{color:var(--blue)}

  /* Slide 3 — pie chart */
  .slide-chart{background:#fff}
  .chart-heading{position:absolute;top:22px;left:30px;font-size:14px;font-weight:700;color:var(--ink)}
  .chart-rule{position:absolute;top:46px;left:0;width:275px;height:2px;background:var(--blue)}
  .chart-copy{position:absolute;top:88px;left:62px;width:140px;font-size:6.6px;line-height:1.5;text-align:justify;color:var(--ink)}
  .chart-copy p+p{margin-top:8px}
  .chart-figure{position:absolute;top:62px;left:225px;width:240px;height:200px}
  .chart-legend{position:absolute;top:256px;left:240px;display:flex;gap:10px;font-size:5.5px;color:var(--muted)}
  .chart-legend span{display:flex;align-items:center;gap:3px}
  .chart-legend i{display:inline-block;width:4px;height:4px}
  .chart-footer{position:absolute;bottom:0;left:0;right:0;height:42px;
    background:linear-gradient(90deg,var(--blue-deep),var(--blue) 60%,var(--blue-bright));
    display:flex;align-items:center;padding:0 28px;color:#fff}
  .footer-url{font-size:7px;flex:1}
  .footer-brand{display:flex;align-items:center;gap:6px;font-size:13px;font-weight:700;flex:1;justify-content:center}
  .footer-brand .brand-square{width:12px;height:12px;background:#fff}
  .footer-page{flex:1;display:flex;justify-content:flex-end}
  .footer-page b{display:flex;align-items:center;justify-content:center;width:26px;height:42px;background:var(--blue-deep);font-size:8px;font-weight:600}
</style>
</head>
<body>
<main class="deck">

  <section class="slide slide-cover">
    <div class="cover-brand"><span class="brand-square"></span><span class="cover-name">Brixom Vale</span></div>
    <p class="cover-url">www.brixomvale.net</p>
  </section>

  <section class="slide slide-title">
    <div class="title-head"><span class="brand-square"></span><span class="title-head-name">Brixom Vale</span></div>
    <div class="title-band">
      <h1 class="title-main">PRESENTATION TITTLE HERE</h1>
      <p class="title-sub">YOUR PRESENTATION &nbsp;SUB TITLE HERE</p>
    </div>
    <div class="title-foot">
      <p class="title-url">www.brixomvale.net</p>
      <p class="title-copy">© 2013 Brixom Vale. All rights reserved.</p>
    </div>
  </section>

  <section class="slide slide-chart">
    <h2 class="chart-heading">BRIXOM VALE PIE CHART SAMPLE HERE</h2>
    <div class="chart-rule"></div>
    <div class="chart-copy">
      <p>The HDRF has forged a courageous and dynamic approach to the methodology of cancer research. By overcoming previous pitfalls that held the industry back, the HDRF has propelled the frontier of multiple myeloma research to a new level.</p>
      <p>Essential to this approach revious pitfalls that held the industry back, the HDRF has propelled the frontier of multiple myeloma research to a new level. are 4 groundbreaking initiatives that have revolutionized the way research and drug development are conducted. With these models, the HDRF can dramatically accelerate the pace at which lifesaving and new life-altering drugs can be brought to patients.</p>
    </div>
    <svg class="chart-figure" viewBox="-120 -100 240 200" role="img" aria-label="Pie chart with four segments">
      <g transform="translate(0,14) scale(1,0.62)">
        <path d="M0 0 L33.8 -72.5 A80 80 0 1 1 -69.3 40 Z" fill="var(--pie-blue-dark)"/>
        <path d="M0 0 L-69.3 40 A80 80 0 0 1 -65.5 -45.9 Z" fill="var(--pie-grey-dark)"/>
        <rect x="-80" y="0" width="160" height="24" fill="var(--pie-blue-dark)" transform="scale(1,1)"/>
      </g>
      <g transform="translate(0,0) scale(1,0.62)">
        <path d="M0 0 L33.8 -72.5 A80 80 0 1 1 -69.3 40 Z" fill="var(--pie-blue)"/>
        <path d="M0 0 L-69.3 40 A80 80 0 0 1 -65.5 -45.9 Z" fill="var(--pie-grey)"/>
        <path d="M0 0 L-65.5 -45.9 A80 80 0 0 1 -27.4 -75.2 Z" fill="var(--pie-silver)"/>
        <path d="M0 0 L-27.4 -75.2 A80 80 0 0 1 33.8 -72.5 Z" fill="var(--pie-sky)"/>
      </g>
    </svg>
    <div class="chart-legend">
      <span><i style="background:var(--pie-blue)"></i>Pie chart 1</span>
      <span><i style="background:var(--pie-grey)"></i>Pie chart 2</span>
      <span><i style="background:var(--pie-silver)"></i>Pie chart 3</span>
      <span><i style="background:var(--pie-sky)"></i>Pie chart 1</span>
    </div>
    <footer class="chart-footer">
      <span class="footer-url">www.brixomvale.net</span>
      <span class="footer-brand"><span class="brand-square"></span>Brixom Vale</span>
      <span class="footer-page"><b>9</b></span>
    </footer>
  </section>

</main>
</body>
</html>
```